Insect-based foods company needs bright, eye catching pouch design for its Green Flour Blend

We are a UK based cricket farm called Molten Acre (www.moltenacre-example.com) and have a retail brand called 'Hoplume' (www.hoplume-example.com). Our main product is 'Green Flour Blend' which we already sell wholesale, through the Hoplume website and on Tradevo UK. At the moment we have designed our own labels which we stick on stand up pouches. This does not look very professional and is very time consuming to do. We are looking to have our pouches custom printed instead and want a new, bold design. We want a design that is bright, colourful, and eye-catching. Our packaging needs to stand out and make the statement - 'this is not an ordinary protein powder'. A few key points:
1. The pouches measure 130mm*225mm
2. We want to keep our existing 'Hoplume' logo
3. We need a design for the front and back. Please use our existing text for the basis of the back of the pack but change it as you see fit.
4. We would like the Union Jack flag to show prominently. Ours is the only cricket powder on the market which is made in the UK and we want to make a big deal about this.
5. The packaging needs to grab peoples attention on the shelf and also on the Tradevo search results page.
6. We intend to use the style of the packaging to re-design our website to match it. This means the theme of the packaging needs to translate well to the overall look of the website.

Target Market(s)

Younger people looking for exiting new protein powder which is sustainable and healthy. Would like to appeal to both men and women.

Font styles to use
Sans Serif

Requirements
Must have
• 1. The pouches measure 130mm*225mm
3. We need a design for the front and back.
4. We would like the Union Jack flag to show somewhere on the packaging. Ours is the only cricket powder on the market which is made in the UK and we want to make a big deal about this.

```html
<!DOCTYPE html>
<html lang="en">
<head>
<meta charset="utf-8">
<title>Hoplume – Green Flour Blend pouch</title>
<link href="https://fonts.googleapis.com/css2?family=Montserrat:wght@600;700&family=Open+Sans:wght@600&display=swap" rel="stylesheet">
<style>
  :root {
    --stage: #07709b;
    --sky-top: #9fd3ea;
    --sky-mid: #e9f4f9;
    --sky-low: #f7fafc;
    --hill-deep: #1c4e80;
    --hill-mid: #2f6f9f;
    --hill-light: #4aa8da;
    --night: #0b1424;
    --slate: #5b8196;
    --ink: #111418;
    --title-blue: #0b5c8f;
    --title-light: #eef1f3;
    --white: #ffffff;
    --zip-line: rgba(60, 110, 140, .35);
    --flag-blue: #1a2a6c;
    --flag-red: #c8102e;
  }
  * { box-sizing: border-box; margin: 0; padding: 0; }
  html, body { width: 1200px; height: 781px; overflow: hidden; }
  body { background: var(--stage); position: relative; font-family: "Montserrat", sans-serif; }

  .pouch {
    position: absolute; top: 44px; width: 362px; height: 632px;
    border-radius: 22px 22px 14px 14px; overflow: hidden;
    background: linear-gradient(180deg, var(--sky-top) 0%, var(--sky-mid) 38%, var(--sky-low) 55%);
  }
  .pouch--dark-title { left: 194px; }
  .pouch--light-title { left: 659px; }

  .zip { position: absolute; left: 18px; right: 18px; height: 1px; background: var(--zip-line); }
  .zip--a { top: 62px; } .zip--b { top: 72px; } .zip--c { top: 84px; }

  .brand {
    position: absolute; left: 0; right: 0; text-align: center;
    font-weight: 700; color: var(--ink); letter-spacing: -.5px; line-height: 1;
  }
  .pouch--dark-title .brand { top: 236px; font-size: 44px; }
  .pouch--light-title .brand { top: 166px; font-size: 42px; }

  .landscape {
    position: absolute; left: 0; right: 0;
    background: linear-gradient(180deg, var(--hill-deep) 0%, var(--hill-mid) 50%, var(--hill-light) 100%);
  }
  .pouch--dark-title .landscape { top: 298px; height: 110px; }
  .pouch--light-title .landscape { top: 360px; height: 102px; }

  .base {
    position: absolute; left: 0; right: 0; bottom: 0;
    background: linear-gradient(110deg, var(--night) 0%, var(--slate) 100%);
  }
  .pouch--dark-title .base { top: 404px; }
  .pouch--light-title .base { top: 458px; }

  .title { position: absolute; text-transform: uppercase; line-height: 1; }
  .title__top { display: block; font-weight: 600; font-size: 34px; letter-spacing: -.5px; }
  .title__main { display: block; font-weight: 700; font-size: 60px; letter-spacing: -1px; margin-top: 4px; }
  .pouch--dark-title .title { left: 56px; top: 424px; color: var(--title-light); }
  .pouch--light-title .title { left: 50px; top: 254px; color: var(--title-blue); }

  .tagline {
    position: absolute; font-family: "Open Sans", sans-serif; font-weight: 600;
    color: var(--white); text-transform: uppercase; letter-spacing: .3px; line-height: 1;
  }
  .pouch--dark-title .tagline { left: 131px; top: 558px; font-size: 14px; }
  .pouch--light-title .tagline { left: 0; right: 0; top: 496px; text-align: center; font-size: 17px; }

  .flag { position: absolute; width: 52px; height: 41px; }
  .pouch--dark-title .flag { left: 58px; top: 550px; }
  .pouch--light-title .flag { left: 64px; top: 556px; width: 50px; height: 39px; }

  .fact { position: absolute; font-family: "Open Sans", sans-serif; font-weight: 600; color: var(--white); white-space: nowrap; line-height: 1; }
  .fact--origin { font-size: 8.5px; }
  .fact--servings, .fact--weight { font-size: 10.5px; }
  .pouch--dark-title .fact--origin { left: 58px; top: 596px; }
  .pouch--dark-title .fact--servings { left: 165px; top: 601px; }
  .pouch--dark-title .fact--weight { left: 263px; top: 596px; }
  .pouch--light-title .fact--origin { left: 64px; top: 599px; }
  .pouch--light-title .fact--servings { left: 170px; top: 600px; }
  .pouch--light-title .fact--weight { left: 262px; top: 595px; }
</style>
</head>
<body>

<section class="pouch pouch--dark-title">
  <span class="zip zip--a"></span><span class="zip zip--b"></span><span class="zip zip--c"></span>
  <p class="brand">hoplume</p>
  <div class="landscape" role="img" aria-label="Layered blue hills under a light sky"></div>
  <div class="base"></div>

  <h1 class="title"><span class="title__top">Green Flour</span><span class="title__main">Blend</span></h1>

  <svg class="flag" viewBox="0 0 60 30" preserveAspectRatio="none" role="img" aria-label="Union Jack flag">
    <clipPath id="flag-clip-a"><path d="M30 15h30v15zv15H0zH0V0zV0h30z"/></clipPath>
    <path d="M0 0v30h60V0z" fill="var(--flag-blue)"/>
    <path d="M0 0l60 30m0-30L0 30" stroke="var(--white)" stroke-width="6"/>
    <path d="M0 0l60 30m0-30L0 30" clip-path="url(#flag-clip-a)" stroke="var(--flag-red)" stroke-width="4"/>
    <path d="M30 0v30M0 15h60" stroke="var(--white)" stroke-width="10"/>
    <path d="M30 0v30M0 15h60" stroke="var(--flag-red)" stroke-width="6"/>
  </svg>
  <p class="tagline">Six-legged superfood</p>
  <p class="fact fact--origin">Farmed in the UK</p>
  <p class="fact fact--servings">10 servings</p>
  <p class="fact fact--weight">100g ℮</p>
</section>

<section class="pouch pouch--light-title">
  <span class="zip zip--a"></span><span class="zip zip--b"></span><span class="zip zip--c"></span>
  <p class="brand">hoplume</p>
  <h1 class="title"><span class="title__top">Green Flour</span><span class="title__main">Blend</span></h1>
  <div class="landscape" role="img" aria-label="Layered blue hills under a light sky"></div>
  <div class="base"></div>

  <p class="tagline">Six-legged superfood</p>

  <svg class="flag" viewBox="0 0 60 30" preserveAspectRatio="none" role="img" aria-label="Union Jack flag">
    <clipPath id="flag-clip-b"><path d="M30 15h30v15zv15H0zH0V0zV0h30z"/></clipPath>
    <path d="M0 0v30h60V0z" fill="var(--flag-blue)"/>
    <path d="M0 0l60 30m0-30L0 30" stroke="var(--white)" stroke-width="6"/>
    <path d="M0 0l60 30m0-30L0 30" clip-path="url(#flag-clip-b)" stroke="var(--flag-red)" stroke-width="4"/>
    <path d="M30 0v30M0 15h60" stroke="var(--white)" stroke-width="10"/>
    <path d="M30 0v30M0 15h60" stroke="var(--flag-red)" stroke-width="6"/>
  </svg>
  <p class="fact fact--origin">Farmed in the UK</p>
  <p class="fact fact--servings">10 servings</p>
  <p class="fact fact--weight">100g ℮</p>
</section>

</body>
</html>
```